Ridgemoor Partners

Need a new website - see more on ridgemoorpartners.com

Target Market(s)

Finance industry = conservative design

Coding

Coded - Design and coding required

Number of Pages Required

5+ page

Requirements
Should not have
• Dear all,
• Please avoid pictures of people on the website (except the "team" of course :-)

```html
<!DOCTYPE html>
<html lang="en">
<head>
<meta charset="utf-8">
<title>Ridgemoor Partners</title>
<link href="https://fonts.googleapis.com/css2?family=Roboto:wght@300;400;500;700;900&display=swap" rel="stylesheet">
<style>
:root{
  --red:#c8161d;
  --red-dark:#9e0f14;
  --ink:#222;
  --muted:#666;
  --light:#eeeeee;
  --dark:#2b2b2b;
  --darker:#1e1e1e;
  --white:#fff;
}
*{box-sizing:border-box;margin:0;padding:0}
html,body{width:1200px;height:2860px;overflow:hidden}
body{font-family:'Roboto',Arial,sans-serif;color:var(--ink);background:var(--white);position:relative}
.abs{position:absolute}

/* hero */
.hero{position:absolute;left:0;top:0;width:1200px;height:800px;overflow:hidden}
.hero-photo{position:absolute;inset:0;height:640px;background:linear-gradient(100deg,#3b4650 0%,#6d7780 35%,#8e969c 55%,#4a5159 80%,#2c3238 100%)}
.hero-shade{position:absolute;inset:0;height:640px;background:linear-gradient(180deg,rgba(0,0,0,.45),rgba(0,0,0,.15) 40%,rgba(0,0,0,.35))}
.brand{position:absolute;left:108px;top:20px;display:flex;align-items:center;gap:14px;color:var(--white);font-weight:700;font-size:22px;line-height:24px;letter-spacing:.5px}
.brand-dot{width:58px;height:58px;border-radius:50%;background:var(--red)}
.nav{position:absolute;right:104px;top:56px;display:flex;gap:38px;list-style:none}
.nav li{color:var(--white);font-size:15px;font-weight:500;letter-spacing:.5px}
.hero-title{position:absolute;left:0;width:1200px;top:228px;text-align:center;color:var(--white);font-weight:700;font-size:56px;letter-spacing:1px}
.hero-sub{position:absolute;left:0;width:1200px;top:300px;text-align:center;color:var(--white);font-weight:500;font-size:36px;line-height:46px}
.arrow{position:absolute;top:280px}
.band{position:absolute;left:0;top:520px}
.service{position:absolute;top:520px;width:360px;text-align:center;color:var(--white)}
.service .icon{width:108px;height:108px;border-radius:50%;background:var(--white);margin:0 auto;display:flex;align-items:center;justify-content:center;box-shadow:0 2px 8px rgba(0,0,0,.25)}
.service h3{margin-top:44px;font-size:21px;font-weight:500;line-height:26px;letter-spacing:.3px}

/* who we are */
.about{position:absolute;left:0;top:800px;width:1200px;height:520px;background:var(--white)}
.about-photo{position:absolute;left:520px;top:0;width:680px;height:520px;background:linear-gradient(120deg,#d8d2c6 0%,#b8aa96 30%,#7c6b58 55%,#c9c3b8 80%,#9a8f80 100%)}
.about-card{position:absolute;left:100px;top:90px;width:420px;height:380px;background:var(--white);border-left:6px solid var(--red);box-shadow:0 4px 18px rgba(0,0,0,.18);padding:34px 30px}
.about-card h2{font-size:40px;font-weight:900;color:#222}
.about-card .lead{margin-top:16px;color:var(--red);font-size:17px;font-weight:500;line-height:23px}
.about-card p.body{margin-top:16px;color:var(--muted);font-size:14px;line-height:21px}
.btn{display:inline-flex;align-items:center;gap:8px;background:var(--red);color:var(--white);font-size:14px;font-weight:700;border-radius:22px;padding:10px 16px;letter-spacing:.3px}
.btn .chev{width:18px;height:18px;border-radius:50%;background:var(--white);display:flex;align-items:center;justify-content:center}
.about-card .btn{margin-top:22px}

/* engagements */
.engagements{position:absolute;left:0;top:1320px;width:1200px;height:300px;background:var(--light)}
.engagements h2{position:absolute;top:84px;width:1200px;text-align:center;font-size:38px;font-weight:500;color:#222}
.partners{position:absolute;top:172px;left:0;width:1200px;display:flex;justify-content:center;align-items:center;gap:70px}
.partner{font-size:36px;color:#222;font-weight:700;letter-spacing:.5px}

/* posts */
.posts h2{position:absolute;left:100px;top:1708px;font-size:40px;font-weight:700;color:#222}
.posts .btn{position:absolute;left:966px;top:1712px;padding:10px 20px}
.card{position:absolute;top:1808px;width:318px;height:300px;background:var(--white);box-shadow:0 2px 10px rgba(0,0,0,.18)}
.card-img{height:160px;position:relative}
.card-tag{position:absolute;left:0;bottom:0;right:0;height:40px;display:flex;align-items:center;background:rgba(200,22,29,.92);color:var(--white)}
.card-tag .date{background:var(--red-dark);height:40px;padding:0 14px;display:flex;align-items:center;font-size:14px;font-weight:700}
.card-tag .title{padding-left:14px;font-size:20px;font-weight:500}
.card p{padding:16px 18px 0;color:var(--muted);font-size:13px;line-height:19px}
.card .more{position:absolute;right:18px;bottom:18px;color:var(--red);font-size:13px;font-weight:700}

/* newsletter */
.newsletter{position:absolute;left:0;top:2200px;width:1200px;height:360px;background:var(--dark)}
.newsletter h2{position:absolute;top:84px;width:1200px;text-align:center;color:var(--white);font-size:38px;font-weight:500;letter-spacing:.5px}
.field{position:absolute;top:154px;width:460px;height:50px;border:1px solid #888;border-radius:4px;background:#3a3a3a;color:#bbb;font-size:16px;padding:14px 16px}
.newsletter .btn{position:absolute;left:540px;top:236px;padding:10px 18px}

/* footer */
.footer{position:absolute;left:0;top:2560px;width:1200px;height:260px;background:var(--darker);color:#cfcfcf}
.col{position:absolute;top:40px;font-size:13px;line-height:24px}
.col h4{color:var(--white);font-size:18px;font-weight:700;margin-bottom:8px}
.col .pin{display:inline-block;width:8px;height:8px;border-radius:50%;background:var(--red);margin-right:8px}
.bottom{position:absolute;left:0;top:2820px;width:1200px;height:40px;background:#151515;color:#999;font-size:12px}
.bottom span{position:absolute;left:100px;top:13px}
.social{position:absolute;right:100px;top:12px;display:flex;gap:12px}
.social i{width:16px;height:16px;border-radius:50%;background:#777;display:block}
</style>
</head>
<body>

<header class="hero">
  <div class="hero-photo" role="img" aria-label="Business meeting in a bright office"></div>
  <div class="hero-shade"></div>
  <div class="brand"><span class="brand-dot"></span><span>RIDGEMOOR<br>PARTNERS</span></div>
  <ul class="nav"><li>HOME</li><li>SERVICES</li><li>CURRENT ENGAGEMENTS</li><li>NEWS</li><li>TEAM</li><li>CONTACT</li></ul>
  <h1 class="hero-title">RIDGEMOOR PARTNERS</h1>
  <p class="hero-sub">We Are A Privately Held Global<br>Investment Holding Group</p>
  <svg class="arrow" style="left:36px" width="24" height="48" viewBox="0 0 24 48"><path d="M20 4 L4 24 L20 44" fill="none" stroke="#fff" stroke-width="3"/></svg>
  <svg class="arrow" style="right:36px" width="24" height="48" viewBox="0 0 24 48"><path d="M4 4 L20 24 L4 44" fill="none" stroke="#fff" stroke-width="3"/></svg>
  <svg class="band" width="1200" height="280" viewBox="0 0 1200 280">
    <path d="M0 120 Q600 20 1200 120 V280 H0Z" fill="#c8161d"/>
    <path d="M0 120 Q600 20 1200 120" fill="none" stroke="#9e0f14" stroke-width="6"/>
  </svg>
  <div class="service" style="left:100px;">
    <div class="icon"><svg width="58" height="58" viewBox="0 0 58 58" fill="none" stroke="#c8161d" stroke-width="4"><circle cx="29" cy="29" r="24"/><circle cx="29" cy="29" r="14"/><circle cx="29" cy="29" r="4" fill="#c8161d"/></svg></div>
    <h3>PRIVATE PLACEMENTS</h3>
  </div>
  <div class="service" style="left:420px;top:496px">
    <div class="icon"><svg width="58" height="58" viewBox="0 0 58 58" fill="none" stroke="#c8161d" stroke-width="4"><path d="M8 20 H46 M38 12 L46 20 L38 28"/><path d="M50 38 H12 M20 30 L12 38 L20 46"/></svg></div>
    <h3>REVERSE MERGERS &amp;<br>ALTERNATIVE OFFERINGS</h3>
  </div>
  <div class="service" style="left:740px;">
    <div class="icon"><svg width="58" height="58" viewBox="0 0 58 58" fill="none" stroke="#c8161d" stroke-width="4"><path d="M29 8 a15 15 0 0 1 9 27 v7 h-18 v-7 a15 15 0 0 1 9 -27z"/><path d="M22 48 h14"/></svg></div>
    <h3>MERGERS &amp; ACQUISITIONS</h3>
  </div>
</header>

<section class="about">
  <div class="about-photo" role="img" aria-label="Business partners shaking hands in an office"></div>
  <div class="about-card">
    <h2>WHO WE ARE?</h2>
    <p class="lead">Ridgemoor Partners is a privately held global investment holding group</p>
    <p class="body">We provide a broad range of financial services to privately held and publicly traded companies across the United States, Europe and Asia. Through our global network, Ridgemoor Partners focuses on high growth sectors, guiding private companies toward public markets and financing companies that are already listed.</p>
    <span class="btn">READ MORE <span class="chev"><svg width="10" height="10" viewBox="0 0 10 10"><path d="M3 1 L7 5 L3 9" fill="none" stroke="#c8161d" stroke-width="2"/></svg></span></span>
  </div>
</section>

<section class="engagements">
  <h2>CURRENT ENGAGEMENTS</h2>
  <div class="partners">
    <span class="partner">CORVANTA</span>
    <span class="partner">HELIOMARK ENERGY</span>
    <span class="partner">LUMISETTE</span>
  </div>
</section>

<section class="posts">
  <h2>LATEST POSTS</h2>
  <span class="btn">VIEW ALL <span class="chev"><svg width="10" height="10" viewBox="0 0 10 10"><path d="M3 1 L7 5 L3 9" fill="none" stroke="#c8161d" stroke-width="2"/></svg></span></span>
  <article class="card" style="left:100px">
    <div class="card-img" role="img" aria-label="Laptop on a desk" style="background:linear-gradient(135deg,#aeb6bd,#5f6870)"><div class="card-tag"><span class="date">Jan 2</span><span class="title">Sed Quis Non Tempora</span></div></div>
    <p>Sed ut perspiciatis unde omnis iste natus error sit voluptatem accusantium doloremque laudantium, totam rem aperiam.</p>
    <span class="more">Read More ›</span>
  </article>
  <article class="card" style="left:441px">
    <div class="card-img" role="img" aria-label="Office meeting scene" style="background:linear-gradient(135deg,#8a7a6a,#3d3a3a)"><div class="card-tag"><span class="date">Jan 2</span><span class="title">Sed Quis Non Tempora</span></div></div>
    <p>Sed ut perspiciatis unde omnis iste natus error sit voluptatem accusantium doloremque laudantium, totam rem aperiam.</p>
    <span class="more">Read More ›</span>
  </article>
  <article class="card" style="left:782px">
    <div class="card-img" role="img" aria-label="Financial charts on a screen" style="background:linear-gradient(135deg,#c9ccd4,#7a8699)"><div class="card-tag"><span class="date">Jan 2</span><span class="title">Sed Quis Non Tempora</span></div></div>
    <p>Sed ut perspiciatis unde omnis iste natus error sit voluptatem accusantium doloremque laudantium, totam rem aperiam.</p>
    <span class="more">Read More ›</span>
  </article>
</section>

<section class="newsletter">
  <svg class="abs" style="left:584px;top:0" width="32" height="14" viewBox="0 0 32 14"><path d="M0 0 L16 14 L32 0Z" fill="#fff"/></svg>
  <h2>SIGN UP FOR OUR NEWSLETTER</h2>
  <div class="field" style="left:136px">Name</div>
  <div class="field" style="left:604px">Email</div>
  <span class="btn">SUBMIT <span class="chev"><svg width="10" height="10" viewBox="0 0 10 10"><path d="M3 1 L7 5 L3 9" fill="none" stroke="#c8161d" stroke-width="2"/></svg></span></span>
</section>

<footer class="footer">
  <div class="col" style="left:120px"><h4>Links</h4>Home<br>Services<br>Current Engagements<br>Team<br>News<br>Contact Us</div>
  <div class="col" style="left:364px"><h4>Beverly Hills</h4><span class="pin"></span>212 N. Alder Court - Suite 410<br><span class="pin" style="visibility:hidden"></span>Beverly Hills, CA 90210<br><span class="pin" style="visibility:hidden"></span>United States<br><span class="pin"></span>+1 310 555 0142</div>
  <div class="col" style="left:672px"><h4>Luxembourg</h4><span class="pin"></span>14, Rue des Tilleuls<br><span class="pin" style="visibility:hidden"></span>L-2450 Luxembourg<br><span class="pin" style="visibility:hidden"></span>Luxembourg<br><span class="pin"></span>+352 20 555 018</div>
  <div class="col" style="left:932px"><h4>London</h4><span class="pin"></span>27 Harlow Mews Place<br><span class="pin" style="visibility:hidden"></span>EC9 7ZZ London<br><span class="pin" style="visibility:hidden"></span>United Kingdom<br><span class="pin"></span>+44 20 7946 0321</div>
</footer>
<div class="bottom"><span>Copyright © 2016, All Rights Reserved</span><div class="social"><i></i><i></i><i></i></div></div>

</body>
</html>
```